Copperfield Roofing Co. business card design

I am a Roofing contractor in Texas. The name of my company is Copperfield Roofing Co. I also offer a few other services (Christmas light installation, gutters, fencing, pressure washing). However my main gig is roofing. Storm restoration and knowledge of the insurance claim process is my specialty.

My colors are black, red and white. I’d like something pretty simple and clean. Modern looking but with a splash of this red tartan pattern.

I have another version of my logo being edited at the moment where the little top part of the F in roofing that’s currently tartan will be changed to just solid red to make it more visible. So if that’s something you can change in your mock up great. But I can provide the full version once the contest is complete

Target Market(s)

Homeowners

Industry/Entity Type

Roofing

Contact Information for Business Card

Derek Pruitt. 682-555-0193. www.copperfield roofing.co Derek@copperfieldroofing.co

Colors
EB3D1F
EC4F4E
F09395
F8D3D4
FCEDEE

Requirements
Nice to have
• Maybe instead of a business address. I could say serving all DFW Texas or something like that. And maybe add a line somewhere saying deductible assistance? Just a thought

```html
<!DOCTYPE html>
<html lang="en">
<head>
<meta charset="UTF-8">
<title>Copperfield Roofing Co. — Business Card</title>
<link rel="stylesheet" href="https://fonts.googleapis.com/css2?family=Montserrat:wght@400;500;700;800&display=swap">
<style>
  :root {
    --red: #e0131a;
    --black: #050505;
    --white: #ffffff;
    --ink: #111111;
    --backdrop: #3b3b3b;
    --divider: #555555;
  }
  * { margin: 0; padding: 0; box-sizing: border-box; }
  html, body {
    width: 1200px; height: 1200px; overflow: hidden;
    background: var(--backdrop);
    font-family: "Montserrat", Arial, sans-serif;
  }
  .sheet {
    width: 1200px; height: 1200px;
    display: flex; flex-direction: column; align-items: center; justify-content: center;
    gap: 44px;
  }
  .card {
    position: relative;
    width: 940px; height: 537px;
    border-radius: 34px;
    overflow: hidden;
  }

  /* Front face */
  .card--front { background: var(--white); }
  .front__top {
    position: absolute; left: 0; top: 0; width: 100%; height: 318px;
    display: flex; align-items: center; justify-content: center;
  }
  .front__rule {
    position: absolute; left: 0; top: 318px; width: 100%; height: 9px;
    background: var(--red);
  }
  .front__bottom {
    position: absolute; left: 0; top: 336px; width: 100%; bottom: 0;
    background: var(--black);
    display: flex; align-items: center;
  }

  .brand {
    display: flex; align-items: center; gap: 22px;
  }
  .brand__mark {
    width: 74px; height: 74px; border-radius: 50%;
    background: var(--red); flex: none;
  }
  .brand__name {
    font-weight: 800; text-transform: uppercase;
    font-size: 40px; letter-spacing: 2px; line-height: 1;
    color: var(--ink);
  }
  .card--back .brand__name { color: var(--white); font-size: 50px; }
  .card--back .brand__mark { width: 96px; height: 96px; }

  .person {
    width: 50%; padding-left: 80px;
    display: flex; align-items: stretch; gap: 18px;
  }
  .person__bar { width: 7px; background: var(--red); }
  .person__name {
    color: var(--red); font-weight: 500; font-size: 38px; text-transform: uppercase;
    letter-spacing: 1px; line-height: 1.1;
  }
  .person__role {
    color: var(--white); font-weight: 400; font-size: 18px; text-transform: uppercase;
    margin-top: 4px;
  }
  .split {
    width: 1px; height: 110px; background: var(--divider);
  }
  .contact {
    list-style: none; padding-left: 56px;
    display: flex; flex-direction: column; gap: 18px;
  }
  .contact__item {
    display: flex; align-items: center; gap: 16px;
    color: var(--white); font-size: 21px; font-weight: 400;
  }
  .contact__icon { width: 24px; height: 24px; flex: none; }

  /* Back face */
  .card--back {
    background: var(--black);
    display: flex; align-items: center; justify-content: center;
  }
</style>
</head>
<body>
<main class="sheet">

  <section class="card card--front" aria-label="Business card front">
    <div class="front__top">
      <div class="brand">
        <span class="brand__mark"></span>
        <span class="brand__name">Copperfield Roofing Co.</span>
      </div>
    </div>
    <div class="front__rule"></div>
    <div class="front__bottom">
      <div class="person">
        <span class="person__bar"></span>
        <div>
          <p class="person__name">Derek Pruitt</p>
          <p class="person__role">Owner</p>
        </div>
      </div>
      <span class="split"></span>
      <ul class="contact">
        <li class="contact__item">
          <svg class="contact__icon" viewBox="0 0 24 24" aria-hidden="true"><path fill="#e0131a" d="M6.6 10.8a15.1 15.1 0 0 0 6.6 6.6l2.2-2.2c.3-.3.7-.4 1-.2 1.1.4 2.3.6 3.6.6.6 0 1 .4 1 1V20c0 .6-.4 1-1 1C10.6 21 3 13.4 3 4c0-.6.4-1 1-1h3.5c.6 0 1 .4 1 1 0 1.3.2 2.5.6 3.6.1.3 0 .7-.2 1z"/></svg>
          682-555-0193
        </li>
        <li class="contact__item">
          <svg class="contact__icon" viewBox="0 0 24 24" aria-hidden="true"><rect x="2" y="5" width="20" height="14" fill="#e0131a"/><path d="M2 5l10 8 10-8" fill="none" stroke="#050505" stroke-width="1.6"/></svg>
          derek@copperfieldroofing.co
        </li>
        <li class="contact__item">
          <svg class="contact__icon" viewBox="0 0 24 24" aria-hidden="true"><g fill="none" stroke="#e0131a" stroke-width="1.8"><circle cx="12" cy="12" r="9.5"/><ellipse cx="12" cy="12" rx="4.2" ry="9.5"/><path d="M2.5 12h19M4 7h16M4 17h16"/></g></svg>
          www.copperfieldroofing.co
        </li>
      </ul>
    </div>
  </section>

  <section class="card card--back" aria-label="Business card back">
    <div class="brand">
      <span class="brand__mark"></span>
      <span class="brand__name">Copperfield Roofing Co.</span>
    </div>
  </section>

</main>
</body>
</html>
```